VELQUARTH - A modern gin bottle label

Design of a bottle label in a modern fresh design. The name of the gin is "VELQUARTH Hollow Batch K7". Please take a look at the velquarth.de website. on the main page of velquarth.de you can breathe the design direction here: 1) the taste of the gin should be composed of 10 botanicals ... an important scent note. ) a distinctive flavor is spicy and fresh 3.) The filling volume is 0.5 liters 4.) the alcohol content is 43% vol. 5.) the variety is called "dry gin" 6.) velquarth stands for "energy" and "love"

Target Market(s)

Alcohol consumer

Colors

Designer to choose colors to be used in the design.

Requirements
Must have
• the velquarth corporate logo must be included, the name of the gin is "VELQUARTH Hollow Batch K7"
Nice to have
• Please use the bottles template in the appendix. (The Black Bottles) they can use the saying "DESTILLED & BOTTLED BY OLD MARROW" in small letters

```html
<!DOCTYPE html>
<html lang="en">
<head>
<meta charset="utf-8">
<title>VELQUARTH Hollow Batch K7 – Label</title>
<link rel="stylesheet" href="https://fonts.googleapis.com/css2?family=Montserrat:wght@600&family=Permanent+Marker&family=Cinzel:wght@400&display=swap">
<style>
  :root {
    --ink: #121212;
    --label-black: #161616;
    --orange: #e2621d;
    --orange-light: #f68a2c;
    --orange-deep: #c8461a;
    --red-orange: #e5421b;
    --silver: #e4e4e4;
    --gold: #d88a2a;
  }
  * { margin: 0; padding: 0; box-sizing: border-box; }
  html, body {
    width: 888px;
    height: 1200px;
    overflow: hidden;
    background: var(--ink);
  }
  .label {
    position: relative;
    width: 888px;
    height: 1200px;
    background: var(--label-black);
  }
  .neck-band {
    position: absolute;
    left: 294px;
    top: 96px;
    width: 300px;
    height: 86px;
    background: linear-gradient(90deg, var(--orange-deep), var(--orange) 45%, var(--orange-light) 70%, var(--orange-deep));
    display: flex;
    align-items: center;
    justify-content: center;
    gap: 10px;
  }
  .neck-band .brand-name {
    font-family: "Montserrat", sans-serif;
    font-weight: 600;
    font-size: 24px;
    letter-spacing: 2px;
    color: var(--silver);
  }
  .brand-mark {
    display: block;
    background: var(--orange);
  }
  .neck-band .brand-mark {
    width: 12px;
    height: 12px;
    background: var(--silver);
  }
  .brand {
    position: absolute;
    top: 360px;
    left: 0;
    width: 888px;
    display: flex;
    flex-direction: column;
    align-items: center;
    gap: 14px;
  }
  .brand .brand-mark {
    width: 26px;
    height: 26px;
  }
  .brand .brand-name {
    font-family: "Montserrat", sans-serif;
    font-weight: 600;
    font-size: 46px;
    letter-spacing: 4px;
    color: var(--silver);
  }
  .moon-scene {
    position: absolute;
    left: 244px;
    top: 520px;
    width: 400px;
    height: 400px;
    border-radius: 50%;
    background: linear-gradient(180deg, var(--orange-light) 0%, var(--orange) 40%, var(--orange-deep) 62%, rgba(22,22,22,0) 86%);
  }
  .variety {
    position: absolute;
    top: 880px;
    left: 0;
    width: 888px;
    text-align: center;
  }
  .variety-name {
    font-family: "Permanent Marker", cursive;
    font-size: 104px;
    line-height: 1;
    letter-spacing: 2px;
    background: linear-gradient(90deg, var(--orange-light), var(--red-orange));
    -webkit-background-clip: text;
    background-clip: text;
    color: transparent;
  }
  .batch {
    margin-top: 4px;
    font-family: "Cinzel", serif;
    font-size: 36px;
    letter-spacing: 2px;
    color: var(--gold);
  }
</style>
</head>
<body>
  <main class="label">
    <div class="neck-band">
      <span class="brand-mark"></span>
      <span class="brand-name">VELQUARTH</span>
    </div>

    <header class="brand">
      <span class="brand-mark"></span>
      <h1 class="brand-name">VELQUARTH</h1>
    </header>

    <div class="moon-scene" role="img" aria-label="Orange full moon with the silhouette of a skeletal hand rising from the ground"></div>

    <section class="variety">
      <h2 class="variety-name">HOLLOW</h2>
      <p class="batch">Batch K7</p>
    </section>
  </main>
</body>
</html>
```